Luminously Grounded Vitality

We want to design a business card that is modern and appealing for an innovative psychedelic telemedicine company that provides at-home ketamine-assisted therapy along with wellness, longevity, and anti-aging medicines. We want to use our deep purple and white plus other colors you can find on our website. We don't have any strict brand guidelines yet so feel free to get creative. We want a very professional, but technology first modern design that will instill trust, peace, calm, but also be attractive to investors in the healthcare and SaaS space.

```html
<!DOCTYPE html>
<html lang="en">
<head>
<meta charset="utf-8">
<title>Luminously Grounded Vitality – Business Card</title>
<link href="https://fonts.googleapis.com/css2?family=Montserrat:wght@400;500;700&display=swap" rel="stylesheet">
<style>
  :root {
    --page-bg: #3a3a3c;
    --purple: #8668ad;
    --purple-deep: #7656a0;
    --purple-soft: #9377b8;
    --pink: #c976a9;
    --white: #ffffff;
  }
  html, body {
    margin: 0;
    width: 1200px;
    height: 1200px;
    overflow: hidden;
    background: var(--page-bg);
    font-family: "Montserrat", sans-serif;
  }
  .canvas {
    position: relative;
    width: 1200px;
    height: 1200px;
  }
  .card {
    position: absolute;
    left: 150px;
    width: 900px;
    height: 514px;
    border-radius: 40px;
    overflow: hidden;
    box-shadow: 0 14px 30px rgba(0,0,0,.35);
  }
  .card-front { top: 60px; background: var(--purple); }
  .card-back {
    top: 626px;
    background: linear-gradient(135deg, var(--purple-deep) 0%, var(--purple-soft) 55%, var(--purple-deep) 100%);
  }
  .card-art { position: absolute; inset: 0; }

  .brand {
    position: absolute;
    display: flex;
    flex-direction: column;
    align-items: center;
    gap: 22px;
  }
  .brand-dot { border-radius: 50%; }
  .brand-name { font-weight: 400; letter-spacing: 1px; }

  .card-front .brand { left: 60px; top: 150px; width: 380px; }
  .card-front .brand-dot { width: 90px; height: 90px; background: var(--purple); }
  .card-front .brand-name { font-size: 54px; color: var(--pink); }

  .card-back .brand { left: 0; right: 0; top: 120px; }
  .card-back .brand-dot { width: 130px; height: 130px; background: #e6e6ea; }
  .card-back .brand-name { font-size: 78px; color: var(--white); }

  .contact {
    position: absolute;
    left: 560px;
    top: 120px;
    color: var(--white);
  }
  .contact-name { margin: 0; font-size: 38px; font-weight: 700; line-height: 1; }
  .contact-role { margin: 4px 0 26px; font-size: 24px; font-weight: 400; letter-spacing: 1px; }
  .contact-list { list-style: none; margin: 0; padding: 0; }
  .contact-item {
    display: flex; align-items: center; gap: 10px;
    font-size: 19px; font-weight: 500; margin-bottom: 12px;
  }
  .contact-icon { width: 22px; height: 22px; flex: none; }
  .social-dot {
    width: 26px; height: 26px; border-radius: 50%;
    border: 2px solid var(--white); box-sizing: border-box; flex: none;
  }
</style>
</head>
<body>
<main class="canvas">

  <section class="card card-front" aria-label="Business card front">
    <svg class="card-art" viewBox="0 0 900 514" aria-hidden="true">
      <path d="M0 0 H420 C560 70 600 300 480 514 H0 Z" fill="var(--pink)"/>
      <path d="M0 0 H395 C530 80 560 310 445 514 H0 Z" fill="var(--white)"/>
      <path d="M0 0 H380 C505 85 540 300 430 514 H0 Z" fill="var(--white)"/>
    </svg>
    <div class="brand">
      <span class="brand-dot"></span>
      <span class="brand-name">Luminously</span>
    </div>
    <div class="contact">
      <h1 class="contact-name">FULL NAME</h1>
      <p class="contact-role">POSITION</p>
      <ul class="contact-list">
        <li class="contact-item">
          <svg class="contact-icon" viewBox="0 0 24 24"><path d="M6.6 10.8a15 15 0 0 0 6.6 6.6l2.2-2.2c.3-.3.7-.4 1-.2 1.1.4 2.3.6 3.6.6.6 0 1 .4 1 1V20c0 .6-.4 1-1 1A17 17 0 0 1 3 4c0-.6.4-1 1-1h3.5c.6 0 1 .4 1 1 0 1.3.2 2.5.6 3.6.1.3 0 .7-.2 1z" fill="var(--white)"/></svg>
          555-010-4782
        </li>
        <li class="contact-item">
          <svg class="contact-icon" viewBox="0 0 24 24"><rect x="2" y="5" width="20" height="14" rx="1" fill="var(--white)"/><path d="M2 6l10 7 10-7" fill="none" stroke="var(--purple)" stroke-width="1.6"/></svg>
          hello@luminously.example
        </li>
        <li class="contact-item">
          <svg class="contact-icon" viewBox="0 0 24 24" fill="none" stroke="var(--white)" stroke-width="1.6"><circle cx="12" cy="12" r="10"/><ellipse cx="12" cy="12" rx="4.5" ry="10"/><path d="M2 12h20M4 7h16M4 17h16"/></svg>
          www.luminously.example
        </li>
        <li class="contact-item">
          <span class="social-dot"></span>
          <span class="social-dot"></span>
          @goluminously
        </li>
      </ul>
    </div>
  </section>

  <section class="card card-back" aria-label="Business card back">
    <div class="brand">
      <span class="brand-dot"></span>
      <span class="brand-name">Luminously</span>
    </div>
  </section>

</main>
</body>
</html>
```